Report template for evaluation reports to be used by non designers

We are looking for a report template that meets all the requirements listed in the attached documents. letter head, logo etc have been enclosed. Its important that the colour integrity is kept, but beyond that options are welcome.
Its important that the document is extremely easy to use and that is able to be adapted to include eatables, figures, pictures, text boxes etc and keep the integrity of the template

Target Market(s)

Governments, Civil society organisations and research institutions

Font styles to use
Sans Serif

Colors
6b449b
876aae
c0c0c0
000000

Requirements
Must have
• Clean, professional, not concluded, modern, must be easy to use
Should not have
• too busy, hard to use

```html
<!DOCTYPE html>
<html lang="en">
<head>
<meta charset="utf-8">
<title>Word Template – Meridian Research Institute</title>
<link href="https://fonts.googleapis.com/css2?family=Source+Sans+3:wght@400;600;700&display=swap" rel="stylesheet">
<style>
  :root{
    --purple:#5b4fa6;
    --purple-soft:#e9e8f8;
    --backdrop:#d9d9d9;
    --ink:#1b1b1b;
    --title:#1d2635;
    --rule:#5b4fa6;
    --muted:#c0c0c0;
  }
  *{box-sizing:border-box;margin:0;padding:0}
  html,body{width:806px;height:1200px;overflow:hidden}
  body{background:var(--backdrop);font-family:"Source Sans 3",sans-serif;color:var(--ink);position:relative}
  .sheet-title{position:absolute;top:14px;left:0;width:806px;text-align:center;font-size:31px;font-weight:400;letter-spacing:.5px;color:var(--title)}
  .page{position:absolute;width:368px;height:520px;background:#fff;box-shadow:0 1px 4px rgba(0,0,0,.25);overflow:hidden}
  .page--cover{left:26px;top:72px}
  .page--toc{left:414px;top:72px}
  .page--three{left:26px;top:636px}
  .page--four{left:414px;top:636px}
  .page-label{position:absolute;width:368px;text-align:center;font-size:19px;color:var(--title)}
  .abs{position:absolute}

  /* cover */
  .cover-bar{left:18px;top:236px;width:331px;height:11px;border-radius:6px;background:var(--purple)}
  .cover-brand{left:0;top:262px;width:368px;text-align:center;font-size:38px;font-weight:600;letter-spacing:6px;color:#111}
  .cover-sub{left:0;top:312px;width:368px;text-align:center;font-size:10px;letter-spacing:3.2px;color:#111}
  .cover-client{left:0;top:376px;width:368px;text-align:center;font-size:25px}
  .cover-date{left:0;top:408px;width:368px;text-align:center;font-size:18px}
  .cover-url{left:0;top:488px;width:368px;text-align:center;font-size:13px}

  /* running header/footer */
  .head-rule{left:0;top:21px;width:297px;height:1.5px;background:var(--rule)}
  .head-brand{left:302px;top:13px;font-size:11px;font-weight:600;letter-spacing:1.6px;color:#111;line-height:1}
  .head-brand small{display:block;font-size:2.6px;letter-spacing:.7px;font-weight:400;margin-top:1px;text-align:center}
  .foot-url{left:18px;top:495px;font-size:6.8px}
  .foot-rule{left:124px;top:499px;width:214px;height:1.2px;background:var(--rule)}
  .foot-num{left:343px;top:495px;font-size:6.8px}

  .section-head{left:17px;font-size:12px;font-weight:700;color:var(--purple);letter-spacing:.1px}
  .section-mark{left:0;width:5px;height:13px;background:var(--purple)}

  /* toc */
  .toc-row{left:19px;width:330px;height:12px;font-size:7.6px;display:flex;align-items:center}
  .toc-label{width:100px}
  .toc-dots{flex:1;border-bottom:1px dashed #555;margin:0 20px 0 0;height:0;position:relative;top:1px}
  .toc-num{width:10px;text-align:right}

  /* page three */
  .body-text{font-size:6.4px;line-height:9.9px;text-align:justify}
  .icon-disc{width:50px;height:50px;border-radius:50%;background:#ebebeb;display:flex;align-items:center;justify-content:center}
  .icon-caption{width:130px;text-align:center;font-size:6.6px;font-weight:600;color:var(--purple)}
  .bullet{left:17px;width:333px;padding-left:12px;font-size:6.4px;line-height:9px;text-align:justify}
  .bullet::before{content:"";position:absolute;left:2px;top:2.5px;width:4px;height:4px;border-radius:50%;background:var(--purple)}
  .note-box{left:18px;top:318px;width:332px;height:120px;background:var(--purple-soft);padding:10px 6px}
  .note-box p{margin-bottom:9px}

  /* page four */
  .step{left:18px;width:332px;border:1px solid var(--purple);display:flex}
  .step-num{width:54px;background:var(--purple);display:flex;align-items:center;justify-content:center}
  .step-num span{width:24px;height:24px;border:1.5px solid #fff;border-radius:50%;color:#fff;font-size:12px;font-weight:600;display:flex;align-items:center;justify-content:center}
  .step-list{list-style:none;padding:0 0 0 8px;display:flex;flex-direction:column;justify-content:center;gap:7px}
  .step-list li{font-size:6.4px;display:flex;align-items:center;gap:5px}
  .photo{left:0;top:322px;width:368px;height:136px;border-top-right-radius:42px;background:linear-gradient(100deg,#3b4a63 0%,#8b8f99 35%,#cfc6bb 60%,#e4e0dc 80%,#6d5a55 100%)}
  .photo-band{left:0;top:458px;width:368px;height:5px;background:var(--purple)}
</style>
</head>
<body>
<h1 class="sheet-title">WORD TEMPLATE</h1>

<!-- Cover -->
<section class="page page--cover">
  <div class="abs cover-bar"></div>
  <div class="abs cover-brand">MERIDIAN</div>
  <div class="abs cover-sub">RESEARCH INSTITUTE</div>
  <div class="abs cover-client">CLIENT NAME</div>
  <div class="abs cover-date">Date, Month, Year</div>
  <div class="abs cover-url">www.meridianresearchinstitute.org</div>
</section>
<div class="page-label" style="left:26px;top:599px">COVER PAGE</div>

<!-- Table of contents -->
<section class="page page--toc">
  <div class="abs head-rule"></div>
  <div class="abs head-brand">MERIDIAN<small>RESEARCH INSTITUTE</small></div>
  <div class="abs section-mark" style="top:72px"></div>
  <div class="abs section-head" style="top:70px">TABLE OF CONTENTS</div>
  <div class="abs toc-row" style="top:98px"><span class="toc-label">Lorem Ipsum is simply</span><span class="toc-dots"></span><span class="toc-num">03</span></div>
  <div class="abs toc-row" style="top:120px"><span class="toc-label">Lorem Ipsum is simply</span><span class="toc-dots"></span><span class="toc-num">04</span></div>
  <div class="abs toc-row" style="top:143px"><span class="toc-label">Lorem Ipsum is simply</span><span class="toc-dots"></span><span class="toc-num">05</span></div>
  <div class="abs toc-row" style="top:165px"><span class="toc-label">Lorem Ipsum is simply</span><span class="toc-dots"></span><span class="toc-num">06</span></div>
  <div class="abs toc-row" style="top:188px"><span class="toc-label">Lorem Ipsum is simply</span><span class="toc-dots"></span><span class="toc-num">07</span></div>
  <div class="abs toc-row" style="top:210px"><span class="toc-label">Lorem Ipsum is simply</span><span class="toc-dots"></span><span class="toc-num">08</span></div>
  <div class="abs toc-row" style="top:233px"><span class="toc-label">Lorem Ipsum is simply</span><span class="toc-dots"></span><span class="toc-num">09</span></div>
  <div class="abs foot-url">www.meridianresearchinstitute.org</div>
  <div class="abs foot-rule"></div>
  <div class="abs foot-num">02</div>
</section>
<div class="page-label" style="left:414px;top:599px">PAGE - 02</div>

<!-- Page three -->
<section class="page page--three">
  <div class="abs head-rule"></div>
  <div class="abs head-brand">MERIDIAN<small>RESEARCH INSTITUTE</small></div>
  <div class="abs section-mark" style="top:45px"></div>
  <div class="abs section-head" style="top:43px">HEADING GOES HERE</div>
  <p class="abs body-text" style="left:17px;top:66px;width:333px">Lorem Ipsum is simply dummy text of the printing and typesetting industry. Lorem Ipsum has been the industry's standard dummy text ever since the 1500s, when an unknown printer took a galley of type and scrambled it to make a type specimen book. It has survived not only five centuries, but also the leap into electronic typesetting, remaining essentially unchanged. It was popularised in the 1960s with the release of Letraset sheets containing Lorem Ipsum passages, and more recently with desktop publishing software like Aldus PageMaker including versions of Lorem Ipsum.</p>

  <div class="abs icon-disc" style="left:39px;top:147px">
    <svg width="32" height="26" viewBox="0 0 32 26" fill="#5b4fa6"><circle cx="16" cy="5" r="3.5"/><circle cx="8" cy="8" r="3"/><circle cx="24" cy="8" r="3"/><circle cx="3" cy="13" r="2.5"/><circle cx="29" cy="13" r="2.5"/><path d="M10 24 L16 10 L22 24Z"/><rect x="3" y="14" width="6" height="10" rx="2"/><rect x="23" y="14" width="6" height="10" rx="2"/><rect x="0" y="17" width="5" height="7" rx="2"/><rect x="27" y="17" width="5" height="7" rx="2"/></svg>
  </div>
  <div class="abs icon-disc" style="left:159px;top:147px">
    <svg width="30" height="28" viewBox="0 0 30 28" fill="#5b4fa6"><rect x="4" y="6" width="8" height="20"/><rect x="13" y="0" width="9" height="26"/><rect x="22" y="12" width="7" height="14"/><rect x="0" y="26" width="30" height="2"/><g fill="#fff"><rect x="15" y="4" width="2" height="3"/><rect x="18" y="4" width="2" height="3"/><rect x="15" y="10" width="2" height="3"/><rect x="18" y="10" width="2" height="3"/><rect x="15" y="16" width="2" height="3"/><rect x="18" y="16" width="2" height="3"/><rect x="24" y="16" width="3" height="2"/><rect x="24" y="21" width="3" height="2"/></g></svg>
  </div>
  <div class="abs icon-disc" style="left:279px;top:147px">
    <svg width="30" height="28" viewBox="0 0 30 28" fill="#5b4fa6"><circle cx="15" cy="3" r="3"/><rect x="11" y="6" width="8" height="5" rx="1.5"/><rect x="14.3" y="11" width="1.4" height="5"/><rect x="4" y="15" width="22" height="1.4"/><rect x="4" y="15" width="1.4" height="4"/><rect x="24.6" y="15" width="1.4" height="4"/><circle cx="5" cy="20" r="2.3"/><circle cx="15" cy="20" r="2.3"/><circle cx="25" cy="20" r="2.3"/><rect x="1" y="23" width="8" height="5" rx="1.5"/><rect x="11" y="23" width="8" height="5" rx="1.5"/><rect x="21" y="23" width="8" height="5" rx="1.5"/></svg>
  </div>
  <div class="abs icon-caption" style="left:-1px;top:204px">Lorem Ipsum is simply dummy</div>
  <div class="abs icon-caption" style="left:119px;top:204px">Lorem Ipsum is simply text</div>
  <div class="abs icon-caption" style="left:239px;top:204px">Lorem Ipsum is simply dummy</div>

  <p class="abs bullet" style="top:236px">Lorem Ipsum is simply dummy text of the printing and typesetting industry. Lorem Ipsum has been the industry's standard dummy text ever since the 1500s.</p>
  <p class="abs bullet" style="top:263px">Lorem Ipsum is simply dummy text of the printing and typesetting industry.</p>

  <div class="abs section-mark" style="top:298px"></div>
  <div class="abs section-head" style="top:296px">HEADING GOES HERE</div>
  <div class="abs note-box body-text">
    <p>Lorem Ipsum is simply dummy text of the printing and typesetting industry. Lorem Ipsum has been the industry's standard dummy text ever since the 1500s, when an unknown printer took a galley of type and scrambled it to make a type specimen book. It has survived not only five centuries, but also the leap into electronic typesetting, remaining essentially unchanged. It was popularised in the 1960s with the release of Letraset sheets containing Lorem Ipsum passages, and more recently with desktop publishing software like Aldus PageMaker including versions of Lorem Ipsum.</p>
    <p>Lorem Ipsum is simply dummy text of the printing and typesetting industry. Lorem Ipsum has been the industry's standard dummy text ever since the 1500s, when an unknown printer took a galley of type and scrambled it to make a type specimen book. It has survived not only five centuries, but also the leap into electronic typesetting, remaining essentially unchanged. It was popularised in the 1960s with the release of Letraset sheets containing Lorem Ipsum passages, and more recently with desktop publishing software like Aldus PageMaker including versions of Lorem Ipsum.</p>
  </div>

  <div class="abs foot-url">www.meridianresearchinstitute.org</div>
  <div class="abs foot-rule"></div>
  <div class="abs foot-num">03</div>
</section>
<div class="page-label" style="left:26px;top:1162px">PAGE - 03</div>

<!-- Page four -->
<section class="page page--four">
  <div class="abs head-rule"></div>
  <div class="abs head-brand">MERIDIAN<small>RESEARCH INSTITUTE</small></div>
  <div class="abs section-mark" style="top:45px"></div>
  <div class="abs section-head" style="top:43px">HEADING GOES HERE</div>

  <div class="abs step" style="top:73px;height:65px">
    <div class="step-num"><span>1</span></div>
    <ul class="step-list">
      <li><svg width="6" height="6" viewBox="0 0 10 10"><circle cx="5" cy="5" r="4.2" fill="none" stroke="#5b4fa6" stroke-width="1.2"/><path d="M3 5.2l1.5 1.5L7.2 3.8" fill="none" stroke="#5b4fa6" stroke-width="1.2"/></svg>Lorem Ipsum is simply dummy text of the printing and typesetting industry.</li>
      <li><svg width="6" height="6" viewBox="0 0 10 10"><circle cx="5" cy="5" r="4.2" fill="none" stroke="#5b4fa6" stroke-width="1.2"/><path d="M3 5.2l1.5 1.5L7.2 3.8" fill="none" stroke="#5b4fa6" stroke-width="1.2"/></svg>Lorem Ipsum is simply dummy text of the printing and typesetting industry.</li>
      <li><svg width="6" height="6" viewBox="0 0 10 10"><circle cx="5" cy="5" r="4.2" fill="none" stroke="#5b4fa6" stroke-width="1.2"/><path d="M3 5.2l1.5 1.5L7.2 3.8" fill="none" stroke="#5b4fa6" stroke-width="1.2"/></svg>Lorem Ipsum is simply dummy text of the printing and typesetting industry.</li>
    </ul>
  </div>
  <div class="abs step" style="top:156px;height:60px">
    <div class="step-num"><span>2</span></div>
    <ul class="step-list">
      <li><svg width="6" height="6" viewBox="0 0 10 10"><circle cx="5" cy="5" r="4.2" fill="none" stroke="#5b4fa6" stroke-width="1.2"/><path d="M3 5.2l1.5 1.5L7.2 3.8" fill="none" stroke="#5b4fa6" stroke-width="1.2"/></svg>Lorem Ipsum is simply dummy text of the printing and typesetting industry.</li>
      <li><svg width="6" height="6" viewBox="0 0 10 10"><circle cx="5" cy="5" r="4.2" fill="none" stroke="#5b4fa6" stroke-width="1.2"/><path d="M3 5.2l1.5 1.5L7.2 3.8" fill="none" stroke="#5b4fa6" stroke-width="1.2"/></svg>Lorem Ipsum is simply dummy text of the printing and typesetting industry.</li>
      <li><svg width="6" height="6" viewBox="0 0 10 10"><circle cx="5" cy="5" r="4.2" fill="none" stroke="#5b4fa6" stroke-width="1.2"/><path d="M3 5.2l1.5 1.5L7.2 3.8" fill="none" stroke="#5b4fa6" stroke-width="1.2"/></svg>Lorem Ipsum is simply dummy text of the printing and typesetting industry.</li>
    </ul>
  </div>
  <div class="abs step" style="top:234px;height:60px">
    <div class="step-num"><span>3</span></div>
    <ul class="step-list">
      <li><svg width="6" height="6" viewBox="0 0 10 10"><circle cx="5" cy="5" r="4.2" fill="none" stroke="#5b4fa6" stroke-width="1.2"/><path d="M3 5.2l1.5 1.5L7.2 3.8" fill="none" stroke="#5b4fa6" stroke-width="1.2"/></svg>Lorem Ipsum is simply dummy text of the printing and typesetting industry.</li>
      <li><svg width="6" height="6" viewBox="0 0 10 10"><circle cx="5" cy="5" r="4.2" fill="none" stroke="#5b4fa6" stroke-width="1.2"/><path d="M3 5.2l1.5 1.5L7.2 3.8" fill="none" stroke="#5b4fa6" stroke-width="1.2"/></svg>Lorem Ipsum is simply dummy text of the printing and typesetting industry.</li>
      <li><svg width="6" height="6" viewBox="0 0 10 10"><circle cx="5" cy="5" r="4.2" fill="none" stroke="#5b4fa6" stroke-width="1.2"/><path d="M3 5.2l1.5 1.5L7.2 3.8" fill="none" stroke="#5b4fa6" stroke-width="1.2"/></svg>Lorem Ipsum is simply dummy text of the printing and typesetting industry.</li>
    </ul>
  </div>

  <div class="abs photo" role="img" aria-label="Photo of colleagues in discussion around a table in a bright office"></div>
  <div class="abs photo-band"></div>

  <div class="abs foot-url">www.meridianresearchinstitute.org</div>
  <div class="abs foot-rule"></div>
  <div class="abs foot-num">04</div>
</section>
<div class="page-label" style="left:414px;top:1162px">PAGE - 04</div>
</body>
</html>
```